Real estate broker business card

Want a modern celan but effective business card for my residential and commercial real estate business. I want the back of the card to advertise my services and to capture business. I have attached the back of my current business card fore ideas
Updates

Target Market(s)

home buyers and seller. commercial buyers and sellers

Industry/Entity Type

Real Estate

Contact Information for Business Card

must have my contact information and my photo

Requirements
Must have
• Lorna Vettridge
• Owner & Qualifying Broker
• Brockhill Real Estate Services
• 555.218.7094
• lorna@brockhillhomes.example
• www.brockhillhomes.example
Nice to have
• metallic
• Business capture text: " Don't buy or lease property without someone looking out for your best interests. I will represent you on your home or investment purchase for FREE!"
• "Home owners, call today to receive a FREE market analysis for your homes value!

```html
<!DOCTYPE html>
<html lang="en">
<head>
<meta charset="utf-8">
<title>Brockhill Real Estate Services – Business Card</title>
<link rel="stylesheet" href="https://fonts.googleapis.com/css2?family=Cinzel:wght@400;600&family=Open+Sans:wght@400;600&display=swap">
<style>
  :root {
    --backdrop: #d9d9d7;
    --card-black: #060708;
    --card-edge: #17191b;
    --teal: #1f7f8c;
    --teal-light: #2f98a6;
    --ink: #111111;
    --contact-grey: #b9bcbf;
    --silver-1: #5c5f62;
    --silver-2: #e9eaeb;
    --silver-3: #ffffff;
    --silver-4: #8d9093;
    --photo-dark: #120d0b;
    --photo-mid: #4a3328;
    --photo-light: #c9b7a8;
  }
  * { margin: 0; padding: 0; box-sizing: border-box; }
  html, body {
    width: 1200px; height: 895px; overflow: hidden;
    background: var(--backdrop);
  }
  .canvas { position: relative; width: 1200px; height: 895px; }

  .card {
    position: absolute; left: 324px; width: 552px; height: 312px;
    border-radius: 16px; overflow: hidden;
    background: linear-gradient(180deg, var(--card-edge) 0%, var(--card-black) 18%, var(--card-black) 100%);
    box-shadow: 0 6px 14px rgba(0,0,0,.35);
  }
  .card--front { top: 108px; }
  .card--back { top: 463px; }

  /* front brand */
  .brand {
    position: absolute; left: 32px; top: 36px;
    display: flex; align-items: center; gap: 12px;
  }
  .brand__dot { width: 44px; height: 44px; border-radius: 50%; background: var(--teal); flex: none; }
  .brand__name {
    font-family: "Cinzel", serif; font-weight: 600; color: var(--teal-light);
    font-size: 17px; line-height: 1.15; letter-spacing: .5px; width: 200px;
  }

  .name-band {
    position: absolute; left: 0; top: 129px; width: 320px; height: 63px;
    background: linear-gradient(90deg, var(--silver-1) 0%, var(--silver-2) 30%, var(--silver-3) 55%, var(--silver-2) 78%, var(--silver-4) 100%);
    text-align: center; padding-left: 60px; padding-top: 9px;
  }
  .name-band__name {
    font-family: "Cinzel", serif; font-weight: 600; font-size: 21px;
    color: var(--ink); letter-spacing: .5px; line-height: 1.1;
  }
  .name-band__title {
    font-family: "Open Sans", sans-serif; font-weight: 600; font-size: 13px;
    color: var(--ink); margin-top: 3px;
  }

  .portrait {
    position: absolute; right: 0; top: 12px; width: 256px; height: 300px;
    background:
      radial-gradient(ellipse 45% 35% at 50% 42%, var(--photo-light) 0%, var(--photo-mid) 60%, transparent 100%),
      radial-gradient(ellipse 60% 30% at 50% 100%, #e8e4e0 0%, transparent 100%),
      linear-gradient(180deg, var(--photo-dark), var(--photo-mid) 70%, var(--photo-dark));
    -webkit-mask-image: linear-gradient(90deg, transparent 0%, #000 14%);
            mask-image: linear-gradient(90deg, transparent 0%, #000 14%);
  }

  .contact {
    position: absolute; left: 32px; top: 228px; list-style: none;
    font-family: "Open Sans", sans-serif; font-size: 13px; color: var(--contact-grey);
  }
  .contact li { display: flex; align-items: center; gap: 6px; height: 19px; }
  .contact svg { width: 13px; height: 13px; fill: none; stroke: var(--teal-light); stroke-width: 1.6; flex: none; }
  .contact .fill { fill: var(--teal-light); stroke: none; }

  /* back */
  .back-brand {
    position: absolute; inset: 0; display: flex; flex-direction: column;
    align-items: center; padding-top: 56px;
  }
  .back-brand__dot { width: 96px; height: 96px; border-radius: 50%; background: var(--teal); }
  .back-brand__name {
    margin-top: 22px; text-align: center;
    font-family: "Cinzel", serif; font-weight: 600; color: var(--teal-light);
    font-size: 26px; line-height: 1.25; letter-spacing: 1px;
  }
</style>
</head>
<body>
<main class="canvas">
  <section class="card card--front">
    <div class="brand">
      <span class="brand__dot"></span>
      <span class="brand__name">Brockhill Real Estate Services</span>
    </div>

    <div class="portrait" role="img" aria-label="Portrait photograph of Lorna Vettridge, smiling, in a white lace top"></div>

    <div class="name-band">
      <div class="name-band__name">Lorna Vettridge</div>
      <div class="name-band__title">Owner &amp; Qualifying Broker</div>
    </div>

    <ul class="contact">
      <li>
        <svg viewBox="0 0 14 14"><path class="fill" d="M1 5c0-2 3-3.5 6-3.5S13 3 13 5l-3 1-1-1.5H5L4 6z"/><path class="fill" d="M3 7h8l1 5H2z"/></svg>
        555.218.7094
      </li>
      <li>
        <svg viewBox="0 0 14 14"><rect class="fill" x="1" y="3" width="12" height="8"/><path d="M1 3l6 5 6-5" stroke="#060708" stroke-width="1.2"/></svg>
        lorna@brockhillhomes.example
      </li>
      <li>
        <svg viewBox="0 0 14 14"><circle cx="7" cy="7" r="5.7"/><ellipse cx="7" cy="7" rx="2.5" ry="5.7"/><path d="M1.3 7h11.4M2.5 4h9M2.5 10h9"/></svg>
        www.brockhillhomes.example
      </li>
    </ul>
  </section>

  <section class="card card--back">
    <div class="back-brand">
      <span class="back-brand__dot"></span>
      <div class="back-brand__name">Brockhill<br>Real Estate Services</div>
    </div>
  </section>
</main>
</body>
</html>
```